Tov Fest Falcons

We are party planning business. We are a team of established individuals and business in party stream businesses like DJ, Caterers, Party supplies, Kids parties, Events & Private Parties and much more. So basically me and business collaborate a team of business or individuals to do clients party in the best way possible.

Target Market(s)

majority of them 16 to 30 -60% to 70 % and 30 to 40 year olds- 30% to 40 %

Industry/Entity Type

Party Planning

Contact Information for Business Card

Tov
Owner & Manager
0481927354
tovfestfalcons@mailbright.example

Requirements
Must have
• front side : Logo and list of services we provide
DJ's, Catering,All party supplies, Tinyvolta and more...just to show what the business is about when anyone looks at the card and at the rear side my details which are already provided.
Should not have
• Dont make it look we do kids party which is just one of the things we do but don't make my business card look like kids party specialist make it more connecting to youngsters and older crowd more

```html
<!DOCTYPE html>
<html lang="en">
<head>
<meta charset="utf-8">
<title>Tov Fest Falcons — Business Card</title>
<link rel="stylesheet" href="https://fonts.googleapis.com/css2?family=Almendra:wght@400;700&family=Arimo:wght@700&display=swap">
<style>
  :root {
    --bg: #e4e4e4;
    --card-white: #ffffff;
    --card-black: #111213;
    --card-red: #d81f26;
    --ink: #111111;
    --faint-disc: #fbeee8;
    --faint-ink: #d4d4d4;
  }
  html, body {
    margin: 0;
    padding: 0;
    width: 1200px;
    height: 900px;
    overflow: hidden;
    background: var(--bg);
  }
  .canvas {
    position: relative;
    width: 1200px;
    height: 900px;
  }
  .card {
    position: absolute;
    top: 295px;
    width: 540px;
    height: 310px;
    border-radius: 24px;
    overflow: hidden;
    background: var(--card-black);
  }
  .card--front { left: 40px; }
  .card--back { left: 620px; }
  .card__shapes {
    position: absolute;
    inset: 0;
    width: 100%;
    height: 100%;
  }

  /* Front */
  .brand {
    position: absolute;
    left: 18px;
    top: 46px;
    width: 240px;
    text-align: center;
  }
  .brand__mark {
    display: block;
    width: 34px;
    height: 34px;
    margin: 0 auto 10px;
    border-radius: 50%;
    background: var(--card-red);
  }
  .brand__name {
    margin: 0;
    font-family: "Almendra", serif;
    font-weight: 700;
    font-size: 38px;
    line-height: 40px;
    color: var(--card-red);
    text-transform: uppercase;
  }
  .brand__tagline {
    margin: 12px 0 0;
    font-family: "Almendra", serif;
    font-weight: 700;
    font-size: 14px;
    line-height: 17px;
    color: var(--ink);
  }
  .services {
    position: absolute;
    right: 22px;
    top: 118px;
    width: 270px;
    margin: 0;
    padding: 0;
    list-style: none;
    text-align: center;
    font-family: "Almendra", serif;
    font-weight: 700;
    font-size: 21px;
    line-height: 44px;
  }
  .services__item--light { color: var(--card-white); }
  .services__item--accent { color: var(--card-red); }

  /* Back */
  .contact {
    position: absolute;
    left: 0;
    right: 0;
    top: 36px;
    text-align: center;
  }
  .contact__name {
    margin: 0;
    font-family: "Almendra", serif;
    font-weight: 700;
    font-size: 38px;
    line-height: 42px;
    color: var(--card-red);
  }
  .contact__role {
    margin: 2px 0 0;
    font-family: "Almendra", serif;
    font-weight: 700;
    font-size: 20px;
    line-height: 24px;
    color: var(--ink);
  }
  .contact__phone {
    margin: 20px 0 0;
    font-family: "Arimo", sans-serif;
    font-weight: 700;
    font-size: 28px;
    line-height: 32px;
    color: var(--ink);
  }
  .contact__email {
    margin: 8px 0 0;
    font-family: "Almendra", serif;
    font-weight: 700;
    font-size: 17px;
    line-height: 20px;
    color: var(--ink);
  }
  .back-tagline {
    position: absolute;
    left: 0;
    right: 0;
    top: 232px;
    margin: 0;
    text-align: center;
    font-family: "Almendra", serif;
    font-weight: 700;
    font-size: 14px;
    line-height: 17px;
    color: var(--faint-ink);
  }
</style>
</head>
<body>
<main class="canvas">

  <section class="card card--front" aria-label="Card front">
    <svg class="card__shapes" viewBox="0 0 540 310" aria-hidden="true">
      <rect width="540" height="310" fill="var(--card-black)"/>
      <path d="M0 0 H300 C268 90 245 200 215 310 H0 Z" fill="var(--card-white)"/>
      <path d="M300 0 L345 0 C305 60 290 110 283 170 C285 110 292 50 308 0 Z" fill="var(--card-red)"/>
    </svg>
    <div class="brand">
      <span class="brand__mark" aria-hidden="true"></span>
      <h1 class="brand__name">Tov Fest<br>Falcons</h1>
      <p class="brand__tagline">Bringing Bold Energy And<br>Flavour To Every Event</p>
    </div>
    <ul class="services">
      <li class="services__item--light">DJ's</li>
      <li class="services__item--accent">Catering</li>
      <li class="services__item--light">All party supplies</li>
      <li class="services__item--accent">Tinyvolta and more...</li>
    </ul>
  </section>

  <section class="card card--back" aria-label="Card back">
    <svg class="card__shapes" viewBox="0 0 540 310" aria-hidden="true">
      <rect width="540" height="310" fill="var(--card-black)"/>
      <ellipse cx="270" cy="120" rx="320" ry="230" fill="var(--card-red)"/>
      <ellipse cx="270" cy="140" rx="290" ry="215" fill="var(--card-white)"/>
      <circle cx="270" cy="140" r="105" fill="var(--faint-disc)"/>
    </svg>
    <div class="contact">
      <p class="contact__name">Tov</p>
      <p class="contact__role">Owner &amp; Manager</p>
      <p class="contact__phone">0481927354</p>
      <p class="contact__email">tovfestfalcons@mailbright.example</p>
    </div>
    <p class="back-tagline" aria-hidden="true">Bringing Bold Energy And<br>Flavour To Every Event</p>
  </section>

</main>
</body>
</html>
```